依頼詳細
新規アプローチの際に持参及び郵送で、内容が1枚で完結出来る内容でお願いします。
①起 国内の生産年齢人口の高齢化問題や、人口減少の課題
特に九州・中国地方では、一部の地域を除き少子高齢化が顕著である事

②承 現在の製造工場での考えうる課題と対策
一部都市部では、留学生の活用、時給の値上げ等により、人員の確保を行っているが、地方では留学生が居ない、そもそも近隣に人がいないと言う問題があり、同様には対応できない状況

③転 しかし、ミルテアでは、1つのケースとして最寄駅から徒歩35分、バスも1日3~4本の工場で1.日本人の採用が可能 2.時給はそれほど上げていない内容 にも関わらず社員の生活環境を整える事で質の高い採用を実現させている、と言う事例があること

④結 今後3年後、5年後を見越した採用計画・手法の見直しの検討材料の1つに、弊社のサービスの実績と、個別の情報提供・提案を受けてみませんか?

と言う上記のポイントを、危機意識を掘り起こしつつ、且つ分かりやすい内容のチラシの作成をお願いしたいします。
記載項目
株式会社ミルテア 〒813-0047 福岡市東区梢台4-27-8
総合エンジニアリング事業(機械・電気・電子・情報) 労働者派遣事業(派40-385207) 有料職業紹介事業(40-57ユ0263)
TEL:092-748-3157 FAX:092-748-3169
HP http://www.kobara-staffnet.com
サイズ
A4
ページ数
片面
希望イメージ
• +5 0 +5
• シンプル
複雑
• 単色
カラフル
• 暗い
明るい
• 日常
高級
• 遊び心
厳粛
• 未来的
伝統的
• 女性的
男性的
希望する色
青系、水色系、黄・オレンジ系
納品ファイル
• 高解像度JPG (.jpg)
• イラストレーター形式 (.ai)
補足説明
会社のHPにも弊社のイメージカラーや紹介が掲載されていますので、宜しければご参照ください。

```html
<!DOCTYPE html>
<html lang="ja">
<head>
<meta charset="utf-8">
<title>株式会社ミルテア 人材戦略のご案内</title>
<link href="https://fonts.googleapis.com/css2?family=Noto+Sans+JP:wght@400;500;700;900&display=swap" rel="stylesheet">
<style>
  :root {
    --blue-deep: #0b4fa3;
    --blue: #1a73c9;
    --sky: #bfe3f6;
    --sky-pale: #e6f4fc;
    --city-top: #cfe6f5;
    --city-mid: #9ec4de;
    --city-low: #6f93ad;
    --yellow: #f5c21b;
    --orange: #f08a1c;
    --teal: #1f9f8f;
    --gold: #c99a2e;
    --red: #d9232d;
    --ink: #222;
    --grey: #777;
    --white: #fff;
  }
  * { box-sizing: border-box; margin: 0; padding: 0; }
  html, body { width: 849px; height: 1200px; overflow: hidden; }
  body {
    position: relative;
    background: var(--white);
    font-family: "Noto Sans JP", sans-serif;
    color: var(--ink);
  }
  .abs { position: absolute; }

  /* hero */
  .hero-city {
    left: 0; top: 0; width: 849px; height: 650px;
    background: linear-gradient(180deg, var(--city-top) 0%, #dcecf6 35%, var(--city-mid) 70%, var(--city-low) 100%);
  }
  .hero-portrait {
    left: 560px; top: 120px; width: 289px; height: 530px;
    background: linear-gradient(180deg, #e9e2da 0%, #2d2f3a 60%, #1d1f27 100%);
    border-radius: 140px 140px 0 0;
  }
  .headline {
    left: 238px; top: 16px; height: 630px; width: 320px;
    writing-mode: vertical-rl;
    font-weight: 900; font-size: 42px; line-height: 1.3;
    letter-spacing: 2px;
    color: var(--blue-deep);
    text-shadow: 0 0 4px var(--white), 0 0 4px var(--white), 0 0 6px var(--white);
  }
  .headline span { display: block; }
  .headline .line-2 { padding-top: 70px; }
  .headline .line-3 { padding-top: 200px; }

  /* story column */
  .story { left: 0; top: 0; width: 222px; height: 1132px; background: var(--sky-pale); }
  .scene {
    position: absolute; left: 6px; width: 210px;
    background: linear-gradient(160deg, var(--sky) 0%, #d8eefa 100%);
    border-radius: 6px;
  }
  .tag {
    position: absolute; font-size: 13px; font-weight: 700;
    background: var(--white); color: var(--blue-deep);
    border: 2px solid var(--blue); border-radius: 12px;
    padding: 1px 9px;
  }
  .tag.warm { border-color: var(--orange); color: var(--orange); }
  .note {
    position: absolute; left: 8px; width: 206px;
    background: var(--white);
    border: 2px solid var(--blue);
    border-radius: 4px;
    padding: 7px 8px;
    font-size: 11.5px; line-height: 1.55;
  }
  .note em { font-style: normal; color: var(--red); font-weight: 700; }
  .note b { color: var(--blue-deep); }
  .chevron { position: absolute; left: 95px; width: 32px; height: 16px; }

  /* needs */
  .needs { left: 240px; top: 656px; width: 600px; height: 138px; display: flex; gap: 10px; justify-content: flex-end; }
  .need {
    width: 176px; height: 138px; border-radius: 6px;
    color: var(--white); text-align: center;
    display: flex; flex-direction: column; align-items: center; justify-content: flex-start;
    padding-top: 12px; font-weight: 700; font-size: 16px; line-height: 1.35;
    box-shadow: 0 2px 4px rgba(0,0,0,.2);
  }
  .need svg { width: 46px; height: 46px; margin-bottom: 8px; }
  .need.blue { background: var(--blue); }
  .need.teal { background: var(--teal); }
  .need.gold { background: var(--gold); }

  .team-photo {
    left: 240px; top: 808px; width: 285px; height: 220px;
    background: linear-gradient(180deg, #f3f5f8 0%, #c7ccd6 55%, #3a3e4a 100%);
  }
  .pitch {
    left: 540px; top: 808px; width: 300px;
    font-size: 12.5px; line-height: 1.7;
  }

  /* company block */
  .company { left: 240px; top: 1034px; width: 600px; }
  .brand { display: flex; align-items: center; gap: 10px; }
  .brand-mark { width: 30px; height: 30px; border-radius: 50%; background: var(--blue); }
  .brand-name { font-size: 26px; font-weight: 700; color: var(--blue-deep); }
  .address { font-size: 13px; margin-left: 14px; }
  .services { font-size: 10px; color: var(--grey); margin-top: 3px; }
  .contact { display: flex; gap: 26px; margin-top: 2px; font-weight: 900; font-size: 30px; color: var(--blue-deep); }
  .contact small { font-size: 14px; font-weight: 700; margin-right: 4px; }
  .contact .fax { color: var(--ink); }

  /* footer */
  .footer {
    left: 0; top: 1132px; width: 849px; height: 68px;
    background: var(--blue-deep);
    display: flex; align-items: center; justify-content: space-between;
    padding: 0 18px; color: var(--white);
  }
  .url { font-size: 24px; font-weight: 900; letter-spacing: .5px; }
  .search { display: flex; height: 36px; }
  .search-field { background: var(--white); color: var(--ink); font-weight: 700; font-size: 16px; padding: 0 12px; display: flex; align-items: center; border: 1px solid #ccc; }
  .search-button { background: #e8e8e8; color: var(--ink); font-size: 15px; font-weight: 700; padding: 0 14px; display: flex; align-items: center; border: 1px solid #bbb; }
</style>
</head>
<body>

  <div class="abs hero-city" role="img" aria-label="福岡の街並みと海を見渡す都市の風景写真"></div>
  <div class="abs hero-portrait" role="img" aria-label="スーツ姿で微笑む女性スタッフの写真"></div>

  <h1 class="abs headline">
    <span class="line-1">人材戦略の名パートナーとして</span>
    <span class="line-2">企業様の安定と活性化に</span>
    <span class="line-3">貢献をいたします。</span>
  </h1>

  <section class="abs story">
    <div class="scene" style="top:6px;height:144px" role="img" aria-label="高齢化と少子化を表すイラスト"></div>
    <span class="tag" style="left:14px;top:14px">高齢化</span>
    <span class="tag warm" style="left:140px;top:14px">少子化</span>
    <p class="note" style="top:156px">今、国内の生産年齢人口の<b>高齢化</b>問題や、<em>人口減少</em>の課題が深刻です。特に九州・中国地方では、一部の地域を除き<b>少子高齢化</b>が顕著です。</p>
    <svg class="chevron" style="top:262px" viewBox="0 0 32 16"><path d="M2 2 L16 14 L30 2" fill="none" stroke="var(--yellow)" stroke-width="4"/></svg>

    <div class="scene" style="top:282px;height:140px" role="img" aria-label="留学生と人員確保に悩む担当者のイラスト"></div>
    <span class="tag warm" style="left:130px;top:292px">留学生</span>
    <span class="tag" style="left:14px;top:350px">人員の確保</span>
    <p class="note" style="top:428px">都市部では<b>留学生の活用</b>や時給の値上げ等で人員の確保を行っていますが、地方では留学生が居ない、そもそも近隣に人がいない等、<em>同様には対応できない</em>状況です。</p>
    <svg class="chevron" style="top:556px" viewBox="0 0 32 16"><path d="M2 2 L16 14 L30 2" fill="none" stroke="var(--yellow)" stroke-width="4"/></svg>

    <div class="scene" style="top:576px;height:118px" role="img" aria-label="高い採用率と実績を表す上昇グラフと担当者のイラスト"></div>
    <span class="tag warm" style="left:120px;top:586px">高い採用率</span>
    <span class="tag" style="left:14px;top:640px">実績</span>
    <p class="note" style="top:700px">しかし、ミルテアでは駅から徒歩35分の工場でも、<b>生活環境を整える</b>事で<em>質の高い採用</em>を実現しています。</p>
    <svg class="chevron" style="top:790px" viewBox="0 0 32 16"><path d="M2 2 L16 14 L30 2" fill="none" stroke="var(--yellow)" stroke-width="4"/></svg>

    <div class="scene" style="top:810px;height:124px" role="img" aria-label="情報提供と採用計画の提案を表すイラスト"></div>
    <span class="tag warm" style="left:110px;top:820px">情報と提案</span>
    <span class="tag" style="left:14px;top:880px">採用計画</span>
    <p class="note" style="top:940px">今後<b>3年後、5年後</b>を見越した採用計画・手法の見直しの検討材料の1つに、弊社のサービスの実績と、<em>個別の情報提供・提案</em>を受けてみませんか?</p>
  </section>

  <div class="abs needs">
    <div class="need blue">
      <svg viewBox="0 0 46 46"><circle cx="23" cy="14" r="9" fill="#fff"/><path d="M7 44 C7 30 39 30 39 44 Z" fill="#fff"/></svg>
      若手の<br>人材が不足<br>している
    </div>
    <div class="need teal">
      <svg viewBox="0 0 46 46"><rect x="5" y="8" width="36" height="34" rx="3" fill="none" stroke="#fff" stroke-width="3"/><line x1="5" y1="17" x2="41" y2="17" stroke="#fff" stroke-width="3"/><path d="M14 29 L21 35 L33 23" fill="none" stroke="#fff" stroke-width="3.5"/></svg>
      社員の<br>定着率を<br>改善したい
    </div>
    <div class="need gold">
      <svg viewBox="0 0 46 46"><circle cx="14" cy="15" r="6" fill="#fff"/><circle cx="32" cy="15" r="6" fill="#fff"/><circle cx="23" cy="22" r="7" fill="#fff"/><path d="M8 44 C8 32 38 32 38 44 Z" fill="#fff"/></svg>
      20名以上の<br>人員が<br>必要になった
    </div>
  </div>

  <div class="abs team-photo" role="img" aria-label="スーツ姿のスタッフ3名の写真"></div>
  <p class="abs pitch">これらの人材に関するソリューションに対し、ミルテアは今までのノウハウと実績をもって最善の解決策をご提案いたします。わたしたちミルテアは企業様の望む人材戦略を的確に把握して、質の高い人材派遣サービスを行っております。</p>

  <div class="abs company">
    <div class="brand">
      <span class="brand-mark"></span>
      <span class="brand-name">株式会社ミルテア</span>
      <span class="address">〒813-0047 福岡市東区梢台4-27-8</span>
    </div>
    <p class="services">総合エンジニアリング事業(機械・電気・電子・情報)　労働者派遣事業(派40-385207)　有料職業紹介事業(40-57ユ0263)</p>
    <div class="contact">
      <span class="tel"><small>TEL</small>092-748-3157</span>
      <span class="fax"><small>FAX</small>092-748-3169</span>
    </div>
  </div>

  <footer class="abs footer">
    <span class="url">HP http://www.kobara-staffnet.com</span>
    <div class="search">
      <span class="search-field">株式会社ミルテア</span>
      <span class="search-button">検索</span>
    </div>
  </footer>

</body>
</html>
```